Create modern and sleek business card for luxury real estate company

We're a "boutique" real estate office looking for a design that gets across a highly modern luxury brand. Blacks and whites are probably the best colors unless we try a silver foil for the logo. I've attached a version of our current logo here. I'd like to swap out the current font on there with Gotham Light Regular.

I'm looking to have one side of the card have the logo with the space for our agents info on the other side.

Target Market(s)

Young professionals in a "luxury" headspace

Industry/Entity Type

Real estate

Contact Information for Business Card

A place for agent name, cell number, website. The slogan "Quietly Redefining Real Estate".

Font styles to use
Other font styles liked:
• Gotham Regular

Colors

Designer to choose only greyscale colors for use in the design.

Requirements
Must have
• Matte black as the background color. Clean lines and use of contrast. A specific design aspect that will use silver foil.
Nice to have
• Up in the air on integrating a QR code
Should not have
• Any houses or other real estate related design (ex: a clip art house)

```html
<!DOCTYPE html>
<html lang="en">
<head>
<meta charset="utf-8">
<title>Meridian Realty – Business Card</title>
<link rel="stylesheet" href="https://fonts.googleapis.com/css2?family=Montserrat:wght@300;400;600&family=Oswald:wght@300&display=swap">
<style>
  :root {
    --backdrop: #1b1c1e;
    --card-black: #000000;
    --ink-light: #f2f2f2;
    --ink-soft: #d8d8d8;
    --rule: #6d6d6d;
    --slogan-ink: #2a2a2a;
    --silver-a: #cfcfcf;
    --silver-b: #f7f7f2;
    --silver-c: #e6e3d6;
  }
  * { margin: 0; padding: 0; box-sizing: border-box; }
  html, body { width: 1200px; height: 1200px; overflow: hidden; background: var(--backdrop); }
  .stage { position: relative; width: 1200px; height: 1200px; font-family: "Montserrat", sans-serif; }

  .card {
    position: absolute; left: 299px; width: 584px; height: 334px;
    background: var(--card-black); overflow: hidden;
    box-shadow: 0 6px 14px rgba(0,0,0,0.45);
  }
  .card--front { top: 249px; }
  .card--back { top: 630px; }

  .brand-circle {
    position: absolute; left: 163px; top: 51px; width: 70px; height: 70px;
    border: 1px solid var(--ink-soft); border-radius: 50%;
  }
  .brand-divider {
    position: absolute; left: 250px; top: 51px; width: 1px; height: 72px; background: var(--rule);
  }
  .brand-name {
    position: absolute; left: 268px; top: 59px;
    font-weight: 300; font-size: 28px; line-height: 29px; letter-spacing: 3px;
    color: var(--ink-light); text-transform: uppercase;
  }

  .agent {
    position: absolute; left: 0; right: 0; top: 170px; text-align: center; color: var(--ink-light);
  }
  .agent__name { font-weight: 300; font-size: 21px; letter-spacing: 0.5px; line-height: 26px; }
  .agent__title { font-weight: 300; font-size: 13px; line-height: 20px; color: var(--ink-soft); }
  .agent__rule {
    position: absolute; top: 203px; height: 1px;
    background: linear-gradient(90deg, transparent, var(--rule) 30%, var(--rule) 70%, transparent);
  }
  .agent__rule--left { left: 108px; width: 145px; }
  .agent__rule--right { left: 327px; width: 145px; }

  .contact {
    position: absolute; left: 0; right: 0; top: 246px; text-align: center;
    font-weight: 300; font-size: 13px; color: var(--ink-light); white-space: nowrap;
  }
  .contact b { font-weight: 600; margin-right: 5px; }
  .contact .sep { margin: 0 7px; }

  .slogan-band {
    position: absolute; left: 0; right: 0; top: 278px; height: 43px;
    background: linear-gradient(100deg, var(--silver-a) 0%, var(--silver-b) 35%, var(--silver-a) 60%, var(--silver-c) 100%);
    display: flex; align-items: center; justify-content: center;
    font-family: "Oswald", sans-serif; font-weight: 300; font-size: 18px;
    letter-spacing: 3.5px; color: var(--slogan-ink); text-transform: uppercase;
  }

  .back-art { position: absolute; inset: 0; }
  .back-name {
    position: absolute; left: 0; right: 0; top: 150px; text-align: center;
    font-weight: 300; font-size: 30px; letter-spacing: 6px; color: var(--ink-light);
  }
</style>
</head>
<body>
<main class="stage">
  <section class="card card--front" aria-label="Business card front">
    <div class="brand-circle"></div>
    <div class="brand-divider"></div>
    <div class="brand-name">Meridian<br>Realty</div>

    <div class="agent">
      <div class="agent__name">AGENT NAME</div>
      <div class="agent__title">Title</div>
    </div>
    <div class="agent__rule agent__rule--left"></div>
    <div class="agent__rule agent__rule--right"></div>

    <p class="contact">
      <b>C:</b>000 555 0142<span class="sep">|</span><b>E:</b>info@meridianrealty.com<span class="sep">|</span><b>W:</b>www.meridianrealty.com
    </p>

    <div class="slogan-band">"Quietly Redefining Real Estate".</div>
  </section>

  <section class="card card--back" aria-label="Business card back">
    <svg class="back-art" width="584" height="334" viewBox="0 0 584 334" aria-hidden="true">
      <defs>
        <linearGradient id="silver-foil" x1="0" y1="0" x2="1" y2="1">
          <stop offset="0" stop-color="#bdbdbd"/>
          <stop offset="0.4" stop-color="#f7f7f2"/>
          <stop offset="0.7" stop-color="#cfcfcf"/>
          <stop offset="1" stop-color="#e6e3d6"/>
        </linearGradient>
      </defs>
      <circle cx="292" cy="170" r="136" fill="none" stroke="url(#silver-foil)" stroke-width="2.5"/>
    </svg>
    <div class="back-name">MERIDIAN</div>
  </section>
</main>
</body>
</html>
```